依頼詳細
現在使っているものを画像データで添付します。
事務所ロゴをフォトショップデータで添付します。

参考に、市販の表紙デザインにはこういったものがあります。(下記リンク)
https://www.kazane-dk.co.jp/store/products/list.php?category_id=23
https://tomoriworks.com/item/certificate/
http://mizuho-kanade.com/front_cover/
A4の紙を綴じるものなので、A3より一回り大きいA3ワイドのレザック紙に印刷しております。こちら302×430mmサイズです。

表紙には、お客様(権利者)の名前と
その下には不動産の表示が入ります。(案件ごとに印刷します)
そのため、こちらを手差し印刷できるよう、高さ5センチ程度の空白を空けておいていただきたいです。

サイズ:A3ワイド(302×430mm)
2つ折り、左開きです。半分に折った部分が表紙となります。

色、デザインの雰囲気等お任せいたします。
公的で固い重要書類をいれるものですが、そういったイメージにはあまり縛られずなるべくオリジナリティのあるものを使いたいと思います。
記載項目
不動産登記権利情報

司法書士ふじさわ事務所
希望イメージ
シンプル 複雑
単色 カラフル
暗い 明るい
日常 高級
遊び心 厳粛
未来的 伝統的
女性的 男性的
希望する色
設定なし
納品ファイル
• イラストレーター形式 (.ai)
補足説明
設定なし
【追記】桐のマークについて
現在使っている権利証表紙には、司法書士バッヂの意匠である五三桐花をいれておりますが、今回は特に使用の指定はしません。
桐のマークを入れる場合については、五三桐でお願いいたします(葉っぱが中央に5枚・左右に3枚ずつの家紋)

(参考)
http://senra-mokudo.com/kamon-c/cate0/kiri/kiri2.html
https://www.ezukan-store.jp/img344/225970_3130817.html
■ 選んだ理由

見た瞬間に目を惹くデザインだと思い、選ばせていただきました。

■ 提案者全員のお礼・コメント

たくさんのご提案をいただき大変嬉しく思っております。
皆様それぞれ、素敵なデザインを考えていただき本当にありがとうございます。

```html
<!DOCTYPE html>
<html lang="ja">
<head>
<meta charset="utf-8">
<title>不動産登記 権利情報 表紙</title>
<link href="https://fonts.googleapis.com/css2?family=Noto+Serif+JP:wght@500;600;700&display=swap" rel="stylesheet">
<style>
  :root {
    --paper: #ffffff;
    --ink: #1a1a1a;
    --office-ink: #2f3440;
    --frame-light: #e6d7c0;
    --frame-mid: #c6a883;
    --frame-dark: #a98a64;
    --box-line: #8c8c8c;
  }
  * { margin: 0; padding: 0; box-sizing: border-box; }
  html, body { width: 861px; height: 1200px; overflow: hidden; background: var(--paper); }
  .cover {
    position: relative;
    width: 861px;
    height: 1200px;
    background: var(--paper);
    font-family: "Noto Serif JP", serif;
    color: var(--ink);
  }
  .ornate-frame {
    position: absolute;
    left: 0; top: 0;
    width: 861px; height: 1200px;
  }
  .cover-title {
    position: absolute;
    left: 0; width: 861px;
    top: 262px;
    text-align: center;
    font-weight: 700;
    font-size: 62px;
    line-height: 76px;
    letter-spacing: 2px;
  }
  .print-area {
    position: absolute;
    left: 224px; top: 468px;
    width: 425px; height: 166px;
    background: var(--paper);
    border: 2px solid var(--box-line);
  }
  .office-block {
    position: absolute;
    left: 178px; top: 870px;
    width: 520px; height: 190px;
    background: var(--paper);
  }
  .office-mark {
    position: absolute;
    left: 18px; top: 22px;
    width: 100px; height: 100px;
    background: var(--office-ink);
  }
  .office-text {
    position: absolute;
    left: 136px; top: 20px;
    color: var(--office-ink);
    text-align: center;
  }
  .office-role { font-size: 26px; font-weight: 600; line-height: 36px; }
  .office-name { font-size: 46px; font-weight: 600; line-height: 60px; letter-spacing: 1px; }
  .office-address { font-size: 14px; font-weight: 500; line-height: 22px; text-align: left; }
  .office-contact { font-size: 16px; font-weight: 500; line-height: 24px; text-align: left; letter-spacing: 0.5px; }
</style>
</head>
<body>
<main class="cover">
  <svg class="ornate-frame" viewBox="0 0 861 1200" role="img" aria-label="金色のバロック調の装飾楕円フレーム">
    <defs>
      <linearGradient id="frame-gold" x1="0" y1="0" x2="1" y2="1">
        <stop offset="0" stop-color="var(--frame-light)"/>
        <stop offset="0.5" stop-color="var(--frame-mid)"/>
        <stop offset="1" stop-color="var(--frame-dark)"/>
      </linearGradient>
    </defs>
    <path fill="url(#frame-gold)" fill-rule="evenodd"
      d="M86 571 a345 519 0 1 0 690 0 a345 519 0 1 0 -690 0 Z
         M178 567 a256 410 0 1 0 512 0 a256 410 0 1 0 -512 0 Z"/>
  </svg>

  <h1 class="cover-title">不動産登記<br>権利情報</h1>

  <div class="print-area" aria-label="権利者名・不動産表示の印刷欄"></div>

  <footer class="office-block">
    <div class="office-mark" aria-hidden="true"></div>
    <div class="office-text">
      <p class="office-role">司法書士・行政書士</p>
      <p class="office-name">ふじさわ事務所</p>
      <p class="office-address">〒062-0014 北海道札幌市南区1条西4丁目12番地</p>
      <p class="office-contact">TEL.0120-48-3170　FAX.0120-48-3171</p>
    </div>
  </footer>
</main>
</body>
</html>
```